Powerpoint: Supplemental Presentation Refresh Ideas

Hello! Our quarterly supplemental and investor presentation reports are in powerpoint. They provide a lot of data - tables, charts and graphs. They are in need of some visual updating.
Our challenge is that our in-house team updates the presentations until the very last minute. We need a template they can manipulate. I'm simply looking for some ideas to help refresh the tired presentations.
Here are some links to examples..... you can also find more here: http://ir.quenvabhold.com/Presentations
http://ir.quenvabhold.com/Cache/IRCache/30651d71-8f14-050b-e87a-7de361f5d4f7.PDF?O=PDF&T=&Y=&D=&FID=30651d71-8f14-050b-e87a-7de361f5d4f7&iid=102970
http://ir.quenvabhold.com/Cache/IRCache/714c2e37-4280-50af-5a3f-c28f3ec702df.PDF?O=PDF&T=&Y=&D=&FID=714c2e37-4280-50af-5a3f-c28f3ec702df&iid=102970
http://ir.quenvabhold.com/Cache/IRCache/5e371c97-e607-4a1f-d889-77c9acae26e6.PDF?O=PDF&T=&Y=&D=&FID=5e371c97-e607-4a1f-d889-77c9acae26e6&iid=102970
Target Market(s)
Analysts

```html
<!DOCTYPE html>
<html lang="en">
<head>
<meta charset="utf-8">
<title>Quenvab Holdings – Supplemental Operating & Financial Data 2Q 2020</title>
<link rel="stylesheet" href="https://fonts.googleapis.com/css2?family=Montserrat:wght@400;600;700&family=Open+Sans:wght@400;600;700&display=swap">
<style>
:root{
  --navy:#233c8c;
  --blue:#2d4fa6;
  --mid:#3f63b8;
  --sky:#7cc4e8;
  --pale:#dce6f5;
  --stripe:#eef2f9;
  --ink:#2b2f3a;
  --grey:#8a90a0;
  --bg:#e9eaee;
  --white:#ffffff;
}
*{margin:0;padding:0;box-sizing:border-box}
html,body{width:1030px;height:1200px;overflow:hidden;background:var(--bg);font-family:"Open Sans",sans-serif;color:var(--ink)}
.canvas{position:relative;width:1030px;height:1200px}
.slide{position:absolute;width:330px;height:185px;background:var(--white);overflow:hidden;box-shadow:0 1px 3px rgba(0,0,0,.12)}
.brand{font-family:"Montserrat",sans-serif;font-weight:700;color:var(--navy);display:flex;align-items:center;gap:3px;letter-spacing:.5px;white-space:nowrap}
.brand .mark{display:inline-block;border-radius:50%;background:var(--navy);flex:none}
.hdr{position:absolute;left:6px;top:6px;right:8px;height:22px}
.hdr .brand{position:absolute;left:2px;top:4px;font-size:6px}
.hdr .brand .mark{width:7px;height:7px}
.hdr .bar{position:absolute;left:46px;right:0;top:1px;height:14px;background:var(--navy);color:#fff;font-family:"Montserrat",sans-serif;font-weight:600;font-size:6.6px;line-height:14px;padding-left:7px;letter-spacing:.2px;white-space:nowrap;overflow:hidden}
.hdr .bar.two{line-height:9px;padding-top:1px}
.hdr .bar small{display:block;font-size:3.2px;line-height:3.4px;font-weight:400}
.hdr .strip{position:absolute;right:0;top:15px;height:5px;width:95px;background:var(--blue);color:#fff;font-size:2.6px;letter-spacing:1.2px;line-height:5px;text-align:center;white-space:nowrap}
.ftr{position:absolute;left:16px;right:16px;bottom:4px;display:flex;justify-content:space-between;font-size:2.8px;letter-spacing:1.3px;color:var(--blue);font-weight:600}
.band{position:absolute;left:0;right:0;background:var(--navy)}
.ph{position:absolute}
.caption{position:absolute;font-size:3.2px;color:#fff;text-align:center}
.sec{position:absolute;font-family:"Montserrat",sans-serif;font-weight:700;font-size:4.5px;color:var(--blue)}
table.grid{position:absolute;border-collapse:collapse;font-size:2.4px;color:var(--ink)}
table.grid th{background:var(--navy);color:#fff;font-weight:600;padding:1.4px 1px;text-align:center}
table.grid td{padding:.9px 1px;text-align:center;border-bottom:.3px solid #fff}
table.grid tr:nth-child(even) td{background:var(--stripe)}
table.grid tr.hl td{background:var(--sky)}
table.grid tr.tot td{background:var(--navy);color:#fff;font-weight:700}
.notes{position:absolute;font-size:2.2px;line-height:2.9px;color:var(--ink)}

/* cover */
.cover{left:303px;top:58px;width:402px;height:226px}
.cover .top{position:absolute;left:0;top:0;width:100%;height:60px;display:flex;align-items:center;justify-content:center}
.cover .top .brand{font-size:15px}
.cover .top .brand .mark{width:16px;height:16px}
.cover .photo{position:absolute;left:0;top:60px;width:100%;height:140px;background:linear-gradient(180deg,#3d5ea8 0%,#2d4c96 55%,#2a4488 100%)}
.cover .title{position:absolute;left:0;right:0;top:110px;text-align:center;color:#fff;font-family:"Montserrat",sans-serif;font-weight:700;font-size:14.5px;line-height:18px}
.cover .sub{position:absolute;left:0;right:0;top:148px;text-align:center;color:#fff;font-family:"Montserrat",sans-serif;font-weight:400;font-size:9px;letter-spacing:2px}

/* toc */
.toc .left{position:absolute;left:0;top:0;width:245px;height:100%}
.toc .right{position:absolute;left:245px;top:0;width:85px;height:100%;background:var(--mid)}
.toc .brand{position:absolute;left:18px;top:8px;font-size:5px}
.toc .brand .mark{width:6px;height:6px}
.toc h4{font-family:"Montserrat",sans-serif;font-size:3.4px;font-weight:700;position:absolute;left:18px}
.toc .para{position:absolute;left:18px;width:180px;font-size:2.2px;line-height:2.9px;text-align:justify}
.toc .card{position:absolute;left:200px;top:14px;width:88px;height:160px;background:#fff;box-shadow:0 1px 3px rgba(0,0,0,.15);padding:8px 9px;font-size:2.6px;line-height:3.4px}
.toc .card b{display:block;font-family:"Montserrat",sans-serif;font-size:3.2px;line-height:4px;margin-top:3px}
.toc .vert{position:absolute;left:302px;top:38px;writing-mode:vertical-rl;color:#fff;font-family:"Montserrat",sans-serif;font-weight:700;font-size:9px;letter-spacing:.5px}
.toc .foot{position:absolute;left:8px;bottom:4px;font-size:2.2px;letter-spacing:1px;color:var(--blue)}

/* company */
.company .left{position:absolute;left:0;top:0;width:163px;height:100%;background:var(--blue);color:#fff}
.company .about{position:absolute;left:10px;top:12px;width:128px;font-size:2.4px;line-height:3.1px;text-align:justify}
.company .badge{position:absolute;border-radius:50%;background:#fff;border:1.5px solid var(--pale)}
.company .pill{position:absolute;left:10px;width:76px;height:9px;border-radius:5px;background:#fff;color:var(--blue);font-family:"Montserrat",sans-serif;font-weight:700;font-size:4.2px;line-height:9px;padding-left:5px}
.company .list{position:absolute;left:10px;font-size:2.3px;line-height:3.2px;display:grid;grid-template-columns:44px 90px}
.company .list span:nth-child(even){color:var(--sky)}
.company .disc{position:absolute;left:12px;bottom:5px;width:140px;text-align:center;font-size:2.3px;line-height:3px}
.company .people{position:absolute;left:172px;top:10px;width:152px;display:grid;grid-template-columns:repeat(3,1fr);row-gap:5px}
.person{font-size:2.6px;line-height:3.2px}
.person .pic{width:24px;height:24px;border-radius:50%;background:linear-gradient(160deg,#c9ced8,#9aa2b2);border:1px solid #fff;box-shadow:0 0 0 .5px #ccd;margin-left:2px;margin-bottom:2px}
.person b{color:var(--blue);font-weight:700;display:block}
.company .contact{position:absolute;left:172px;top:156px;width:150px;display:grid;grid-template-columns:14px 60px 70px;font-size:2.3px;line-height:2.9px}
.company .contact b{color:var(--blue)}

/* hex */
.hex{position:absolute;width:48px;height:54px}
.hex .t{position:absolute;inset:0;display:flex;flex-direction:column;align-items:center;justify-content:center;color:var(--navy);font-family:"Montserrat",sans-serif;font-weight:700;text-align:center}

.legend{position:absolute;font-size:2.4px;line-height:4.2px}
.legend i{display:inline-block;width:3px;height:3px;margin-right:2px;vertical-align:middle}
</style>
</head>
<body>
<div class="canvas">

  <!-- Cover -->
  <section class="slide cover">
    <div class="top"><div class="brand"><span class="mark"></span>QUENVAB</div></div>
    <div class="photo" role="img" aria-label="Photograph of a senior living community building with porch and lawn, tinted blue"></div>
    <div class="title">Supplemental Operating &amp;<br>Financial Data</div>
    <div class="sub">SECOND QUARTER 2020</div>
  </section>

  <!-- Table of contents -->
  <section class="slide toc" style="left:13px;top:417px">
    <div class="left">
      <div class="brand"><span class="mark"></span>QUENVAB</div>
      <h4 style="top:22px">FORWARD-LOOKING STATEMENTS</h4>
      <p class="para" style="top:27px">This supplemental information contains forward-looking statements within the meaning of the securities laws. Statements that are not purely historical may be forward-looking. You can identify some of the forward-looking statements by their use of words such as believes, expects, may, will, should, seeks, intends, plans, estimates or anticipates. Forward-looking statements involve inherent risks and uncertainties regarding events, conditions and financial trends that may affect our future plans of operation, business strategy, results of operations and financial position. A number of important factors could cause actual results to differ materially from those included within or contemplated by such statements, including the status of the economy, the status of capital markets, our access to capital, the income and returns available from investments in health care related real estate, the ability of our borrowers and lessees to meet their obligations, our reliance on a few major operators, competition faced by our borrowers and lessees within the health care industry, regulation of the health care industry by federal, state and local governments, changes in reimbursement rates, compliance with and changes to regulations and payment policies, our ability to maintain our status as a real estate investment trust, the relative illiquidity of our real estate investments, potential limitations on our remedies when mortgage loans default, and risks and liabilities in connection with properties owned through limited liability companies and partnerships. For a discussion of these and other factors please see the risk factors in our annual report. We do not undertake any responsibility to update or revise any of these forward-looking statements.</p>
      <h4 style="top:137px">NON-GAAP INFORMATION</h4>
      <p class="para" style="top:142px">This supplemental information contains certain non-GAAP information including EBITDAre, adjusted EBITDAre, FFO, FFO excluding non-recurring items, adjusted interest coverage ratio and adjusted fixed charges coverage ratio. A reconciliation of this non-GAAP information is provided in this supplemental information and is also available at quenvabhold.com.</p>
      <div class="foot">SUPPLEMENTAL INFORMATION 2Q 2020</div>
    </div>
    <div class="right"></div>
    <div class="card">
      <b>COMPANY</b>Company Information &amp; Leadership 3
      <b>INVESTMENTS</b>Execution of Growth Strategy 4<br>Real Estate Activities<br>Acquisitions and Loan Originations 5<br>Joint Ventures 6<br>De Novo Development 7<br>Expansions and Renovations 8<br>Lease-Up and Lease-Up History 9-10<br>Capital Recycling 11
      <b>PORTFOLIO</b>Portfolio Overview 12<br>Portfolio Metrics 13<br>Portfolio Diversification<br>Geography, MSA, Age of Portfolio 14-15<br>Operators 16<br>Maturity 17
      <b>FINANCIAL</b>Enterprise Value 18<br>Debt Metrics 19<br>Debt Maturity 20<br>Financial Data Summary 21-22<br>Income Statement Data 23<br>Consolidated Balance Sheets 24<br>Funds from Operations 25-26
      <b>GLOSSARY</b>Glossary 27-28
    </div>
    <div class="vert">TABLE OF CONTENTS</div>
  </section>

  <!-- Company information -->
  <section class="slide company" style="left:351px;top:417px">
    <div class="left">
      <p class="about">Founded in 1992, Quenvab Holdings, Inc. is a self-administered real estate investment trust investing in seniors housing and health care properties primarily through sale-leaseback transactions, mortgage financing and mezzanine financing. Our portfolio encompasses Skilled Nursing Facilities, Assisted Living Communities, Independent Living Communities, Memory Care Communities and combinations thereof. Our main objective is to build and grow a diversified portfolio that creates and sustains shareholder value while providing our stockholders current distribution income. To meet this objective, we seek properties operated by regional operators, ideally offering upside and portfolio diversification by geography, operator, property type and investment vehicle. For more information, visit quenvabhold.com.</p>
      <div class="pill" style="top:66px">BOARD OF DIRECTORS</div>
      <div class="list" style="top:80px">
        <span>Elena Marsh</span><span>Chairman</span>
        <span>Carl Renfrew</span><span>Lead Independent Director</span>
        <span>Victor Lenz</span><span>Nominating &amp; Governance Committee Chair</span>
        <span>Helen Corby</span><span>Audit Committee Chair</span>
        <span>Martin Vale</span><span>Compensation Committee Chair</span>
      </div>
      <div class="pill" style="top:110px">ANALYSTS</div>
      <div class="list" style="top:125px">
        <span>Adam Pryce</span><span>Hallmark Capital</span>
        <span>Sean Albright</span><span>Northgate Markets</span>
        <span>Eli Grant</span><span>Harborline Securities</span>
        <span>Ross Kemper</span><span>Summit Lane Partners</span>
        <span>Paul Dreyer</span><span>Ridgeway Securities</span>
        <span>Kofi Mensah</span><span>Eastfield Securities</span>
        <span>Jake Dorsey</span><span>Crestmoor Markets</span>
        <span>Lyle Foster</span><span>Oakbridge Securities</span>
        <span>Brett Nolan</span><span>Linden Bay Securities</span>
      </div>
      <p class="disc">Any opinions, estimates, or forecasts regarding our performance made by the analysts listed above do not represent the opinions, estimates, and forecasts of the company or its management.</p>
    </div>
    <div class="badge" style="left:143px;top:10px;width:22px;height:22px"></div>
    <div class="badge" style="left:143px;top:38px;width:22px;height:22px"></div>
    <div class="people">
      <div class="person"><div class="pic" role="img" aria-label="Portrait of Elena Marsh"></div><b>Elena Marsh</b>Chairman and<br>Chief Executive Officer</div>
      <div class="person"><div class="pic" role="img" aria-label="Portrait of Dana Whitfield"></div><b>Dana Whitfield</b>Executive Vice President,<br>CFO and Secretary</div>
      <div class="person"><div class="pic" role="img" aria-label="Portrait of Rory Castell"></div><b>Rory Castell</b>Executive Vice President,<br>Chief Investment Officer</div>
      <div class="person"><div class="pic" role="img" aria-label="Portrait of Nina Parekh"></div><b>Nina Parekh</b>Senior Vice President,<br>Controller and Treasurer</div>
      <div class="person"><div class="pic" role="img" aria-label="Portrait of Glen Ashby"></div><b>Glen Ashby</b>Senior Vice President,<br>Managing Director of<br>Business Development</div>
      <div class="person"><div class="pic" role="img" aria-label="Portrait of Owen Tanaka"></div><b>Owen Tanaka</b>Vice President,<br>Director of Taxes</div>
      <div class="person"><div class="pic" role="img" aria-label="Portrait of Lacey Brandt"></div><b>Lacey Brandt</b>Vice President,<br>Marketing</div>
      <div class="person"><div class="pic" role="img" aria-label="Portrait of Miles Oakridge"></div><b>Miles Oakridge</b>Vice President,<br>Asset Management</div>
      <div class="person"><div class="pic" role="img" aria-label="Portrait of Trent Halloway"></div><b>Trent Halloway</b>Vice President,<br>Investments</div>
    </div>
    <div class="contact">
      <svg width="10" height="12" viewBox="0 0 10 12"><rect x="1" y="1" width="8" height="10" fill="none" stroke="#233c8c" stroke-width=".8"/><path d="M3 3h1M6 3h1M3 5h1M6 5h1M3 7h1M6 7h1" stroke="#233c8c" stroke-width=".8"/></svg>
      <span><b>QUENVAB HOLDINGS, INC.</b><br>4100 Alder Crest Drive<br>Suite 300<br>Fairmont, CA 90000<br>555-010-2200<br>quenvabhold.com</span>
      <span><b>TRANSFER AGENT</b><br>Keystone Share Registry<br>and Trust Company<br>77 Harbor Avenue<br>Lakeport, NY 10000<br>555-010-4400</span>
    </div>
  </section>

  <!-- Growth strategy -->
  <section class="slide" style="left:690px;top:417px">
    <div class="hdr"><div class="brand"><span class="mark"></span>QUENVAB</div><div class="bar">EXECUTION OF GROWTH STRATEGY</div><div class="strip">SUPPLEMENTAL INFORMATION 2Q 2020</div></div>
    <div style="position:absolute;left:20px;top:41px;width:292px;height:134px;background:#fff;box-shadow:0 0 3px rgba(0,0,0,.15)"></div>
    <svg style="position:absolute;left:20px;top:41px" width="292" height="134" viewBox="0 0 292 134" font-family="Open Sans, sans-serif">
      <text x="146" y="9" text-anchor="middle" font-size="4.6" fill="#2d4fa6" font-weight="600">$1.5 Billion in Total Investments Underwritten</text>
      <g stroke="#e2e5ec" stroke-width=".4"><line x1="10" y1="20" x2="284" y2="20"/><line x1="10" y1="40" x2="284" y2="40"/><line x1="10" y1="60" x2="284" y2="60"/><line x1="10" y1="80" x2="284" y2="80"/><line x1="10" y1="100" x2="284" y2="100"/></g>
      <g fill="#233c8c">
        <rect x="12" y="107" width="20" height="15"/><rect x="36" y="104" width="20" height="18"/><rect x="60" y="83" width="20" height="39"/><rect x="84" y="100" width="20" height="22"/><rect x="108" y="118" width="20" height="4"/><rect x="132" y="56" width="20" height="66"/><rect x="156" y="99" width="20" height="23"/><rect x="180" y="106" width="20" height="16"/><rect x="204" y="109" width="20" height="13"/><rect x="228" y="109" width="20" height="13"/><rect x="252" y="120" width="20" height="2"/>
      </g>
      <g fill="#7cc4e8">
        <rect x="36" y="103" width="20" height="1"/><rect x="60" y="72" width="20" height="11"/><rect x="84" y="93" width="20" height="7"/><rect x="108" y="117" width="20" height="1"/><rect x="132" y="38" width="20" height="18"/><rect x="156" y="93" width="20" height="6"/><rect x="180" y="102" width="20" height="4"/><rect x="204" y="105" width="20" height="4"/><rect x="228" y="106" width="20" height="3"/>
      </g>
      <g font-size="3" fill="#fff" text-anchor="middle">
        <text x="22" y="116">94</text><text x="46" y="114">109</text><text x="70" y="104">245</text><text x="94" y="112">133</text><text x="142" y="91">414</text><text x="166" y="112">142</text><text x="190" y="115">103</text><text x="214" y="117">80</text><text x="238" y="117">81</text>
        <text x="70" y="79" fill="#233c8c">68</text><text x="94" y="98" fill="#233c8c">44</text><text x="142" y="48" fill="#233c8c">112</text><text x="166" y="97" fill="#233c8c">39</text>
      </g>
      <g font-size="3" fill="#555" text-anchor="middle">
        <text x="22" y="128">2010</text><text x="46" y="128">2011</text><text x="70" y="128">2012</text><text x="94" y="128">2013</text><text x="118" y="128">2014</text><text x="142" y="128">2015</text><text x="166" y="128">2016</text><text x="190" y="128">2017</text><text x="214" y="128">2018</text><text x="238" y="128">2019</text><text x="262" y="128">2020</text>
      </g>
    </svg>
    <div class="legend" style="left:70px;top:170px"><i style="background:var(--navy)"></i>Total investment (excludes non-controlling partner contributions) &nbsp;&nbsp; <i style="background:var(--sky)"></i>Development / Expansions / Renovations</div>
    <div class="ftr"><span>INVESTMENTS</span><span>PAGE | 4</span></div>
  </section>

  <!-- Acquisitions & loans -->
  <section class="slide" style="left:13px;top:612px">
    <div class="hdr"><div class="brand"><span class="mark"></span>QUENVAB</div><div class="bar">REAL ESTATE ACTIVITIES – ACQUISITIONS AND LOAN ORIGINATIONS</div><div class="strip">SUPPLEMENTAL INFORMATION 2Q 2020</div></div>
    <div class="sec" style="left:10px;top:30px">ACQUISITIONS</div>
    <table class="grid" style="left:10px;top:37px;width:312px">
      <tr><th>DATE</th><th># OF PROPERTIES</th><th>PROPERTY TYPE</th><th># BEDS/UNITS</th><th>LOCATION</th><th>OPERATOR</th><th>DATE OF CONSTRUCTION</th><th>INITIAL CASH YIELD</th><th>PURCHASE PRICE</th><th>ADD'L COMMITMENT</th></tr>
      <tr><td>2018</td><td>1</td><td>ALF</td><td>78</td><td>Tulsa, OK</td><td>Meridian</td><td>2016</td><td>7.3%</td><td>$14,500</td><td>–</td></tr>
      <tr><td>6/18</td><td>1</td><td>MC</td><td>64</td><td>Salem, OR</td><td>Harbor</td><td>2015</td><td>7.0%</td><td>$12,200</td><td>–</td></tr>
      <tr><td>8/18</td><td>2</td><td>ILF</td><td>110</td><td>Boise, ID</td><td>Meridian</td><td>2014</td><td>6.8%</td><td>$21,900</td><td>$1,000</td></tr>
      <tr class="hl"><td>2019</td><td>–</td><td>–</td><td>–</td><td>–</td><td>–</td><td>–</td><td>–</td><td>–</td><td>–</td></tr>
      <tr><td>1/19</td><td>1</td><td>SNF</td><td>120</td><td>Ames, IA</td><td>Harbor</td><td>2012</td><td>7.5%</td><td>$16,800</td><td>–</td></tr>
      <tr><td>4/19</td><td>1</td><td>ALF</td><td>90</td><td>Mesa, AZ</td><td>Meridian</td><td>2017</td><td>7.0%</td><td>$18,300</td><td>–</td></tr>
      <tr><td>6/19</td><td>1</td><td>MC</td><td>56</td><td>Waco, TX</td><td>Harbor</td><td>2018</td><td>7.3%</td><td>$11,400</td><td>$500</td></tr>
      <tr><td>9/19</td><td>1</td><td>ALF</td><td>72</td><td>Reno, NV</td><td>Meridian</td><td>2016</td><td>7.1%</td><td>$13,700</td><td>–</td></tr>
      <tr><td>12/19</td><td>1</td><td>ILF</td><td>88</td><td>Erie, PA</td><td>Harbor</td><td>2013</td><td>6.9%</td><td>$15,100</td><td>–</td></tr>
      <tr class="hl"><td>Total</td><td>9</td><td>–</td><td>778</td><td>–</td><td>–</td><td>–</td><td>7.1%</td><td>$123,900</td><td>$1,500</td></tr>
    </table>
    <div class="notes" style="left:10px;top:104px;width:312px">(1) Commitments may include capital improvement or development allowances for approved projects.<br>(2) See page 7 for development activities and joint venture details for these projects.<br>(3) Acquired a parcel of land adjacent to an existing community for a future expansion.<br>(4) Escalated by 2% each year thereafter under the master lease agreement.</div>
    <div class="sec" style="left:10px;top:119px">LOAN ORIGINATIONS</div>
    <table class="grid" style="left:10px;top:126px;width:312px">
      <tr><th>DATE</th><th># OF PROPERTIES</th><th>PROPERTY TYPE</th><th>LOCATION</th><th>LOAN TYPE</th><th>MATURITY DATE</th><th>OPERATOR</th><th>ORIGINATION</th><th>FUNDED AT ORIGINATION</th><th>STATED RATE</th></tr>
      <tr><td>3/19</td><td>1</td><td>SNF</td><td>Flint, MI</td><td>Mortgage</td><td>2045</td><td>Meridian</td><td>$7,500</td><td>$7,500</td><td>9.4%</td></tr>
      <tr><td>6/19</td><td>1</td><td>ALF</td><td>Lima, OH</td><td>Mezz</td><td>2024</td><td>Harbor</td><td>$3,200</td><td>$3,200</td><td>10.0%</td></tr>
      <tr><td>9/19</td><td>1</td><td>SNF</td><td>Troy, MI</td><td>Mortgage</td><td>2045</td><td>Meridian</td><td>$8,100</td><td>$6,900</td><td>9.4%</td></tr>
      <tr class="tot"><td>Total</td><td>3</td><td></td><td></td><td></td><td></td><td></td><td>$18,800</td><td>$17,600</td><td>9.5%</td></tr>
      <tr><td>2/20</td><td>1</td><td>ALF</td><td>Kent, WA</td><td>Mezz</td><td>2025</td><td>Harbor</td><td>$2,000</td><td>$2,000</td><td>10.0%</td></tr>
    </table>
    <div class="notes" style="left:10px;top:167px;width:312px">(1) Funded additional loan proceeds under existing mortgage loans for capital improvements.</div>
    <div class="ftr"><span>INVESTMENTS</span><span>PAGE | 5</span></div>
  </section>

  <!-- De novo development -->
  <section class="slide" style="left:351px;top:612px">
    <div class="hdr"><div class="brand"><span class="mark"></span>QUENVAB</div><div class="bar">REAL ESTATE ACTIVITIES – DE NOVO DEVELOPMENT</div><div class="strip">SUPPLEMENTAL INFORMATION 2Q 2020</div></div>
    <table class="grid" style="left:10px;top:34px;width:312px">
      <tr><th>DATE</th><th># OF PROPERTIES</th><th>PROPERTY TYPE</th><th>LOCATION</th><th>LOAN TYPE</th><th>MATURITY DATE</th><th>OPERATOR</th><th>ORIGINATION</th><th>FUNDED</th><th>REMAINING</th></tr>
      <tr><td>3/19</td><td>1</td><td>SNF</td><td>Flint, MI</td><td>Const.</td><td>2024</td><td>Meridian</td><td>$9,100</td><td>$6,200</td><td>$2,900</td></tr>
      <tr><td>6/19</td><td>1</td><td>ALF</td><td>Lima, OH</td><td>Const.</td><td>2025</td><td>Harbor</td><td>$8,400</td><td>$4,100</td><td>$4,300</td></tr>
      <tr><td>9/19</td><td>1</td><td>MC</td><td>Kent, WA</td><td>Const.</td><td>2025</td><td>Harbor</td><td>$6,600</td><td>$2,700</td><td>$3,900</td></tr>
      <tr class="hl"><td>Total</td><td>3</td><td></td><td></td><td></td><td></td><td></td><td>$24,100</td><td>$13,000</td><td>$11,100</td></tr>
    </table>
    <div class="notes" style="left:10px;top:62px;width:312px">(1) Includes purchase of land and initial improvement funding, if applicable, and development commitment.<br>(2) Remaining commitment is calculated as investment commitment less total project basis.<br>(3) Completion of this medical resort in Independence is scheduled for the fall of 2020.</div>
    <div class="band" style="top:133px;height:45px"></div>
    <div class="ph" role="img" aria-label="Photograph of a single-storey care building under construction with siding complete" style="left:32px;top:84px;width:119px;height:68px;background:linear-gradient(170deg,#9fb4cf 0%,#8c8f86 55%,#6f6a5c 100%)"></div>
    <div class="ph" role="img" aria-label="Photograph of timber wall framing on a construction site" style="left:182px;top:84px;width:119px;height:68px;background:linear-gradient(170deg,#b8c7d8 0%,#c39a6f 50%,#8a7158 100%)"></div>
    <div class="caption" style="left:100px;top:158px;width:130px">Crestview Medical Resort<br>Independence, MO</div>
    <div class="ftr"><span>INVESTMENTS</span><span>PAGE | 6</span></div>
  </section>

  <!-- Expansions -->
  <section class="slide" style="left:690px;top:612px">
    <div class="hdr"><div class="brand"><span class="mark"></span>QUENVAB</div><div class="bar two">REAL ESTATE ACTIVITIES – EXPANSIONS &amp; RENOVATIONS<small>(DOLLAR AMOUNTS IN THOUSANDS)</small></div><div class="strip">SUPPLEMENTAL INFORMATION 2Q 2020</div></div>
    <div class="sec" style="left:10px;top:30px">MORTGAGE LOANS</div>
    <table class="grid" style="left:10px;top:37px;width:312px">
      <tr><th>EST. RATE DATE</th><th>COMMIT. YEAR</th><th>PROJECT TYPE</th><th>LOCATION</th><th>OPERATOR</th><th># OF PROJ.</th><th>PROP. TYPE</th><th>INITIAL YIELD</th><th>COMMIT.</th><th>2Q FUNDING</th><th>FUNDED</th><th>REMAINING</th></tr>
      <tr><td>–</td><td>2018</td><td>Renov.</td><td>Flint, MI</td><td>Meridian</td><td>1</td><td>SNF</td><td>9.41%</td><td>$4,300</td><td>$133</td><td>$1,936</td><td>$2,364</td></tr>
      <tr><td>–</td><td>2018</td><td>Renov.</td><td>Troy, MI</td><td>Meridian</td><td>1</td><td>SNF</td><td>9.41%</td><td>$1,700</td><td>$21</td><td>$971</td><td>$729</td></tr>
      <tr><td>–</td><td>2018</td><td>Renov.</td><td>Holt, MI</td><td>Meridian</td><td>1</td><td>SNF</td><td>9.41%</td><td>$500</td><td>$221</td><td>$711</td><td>$239</td></tr>
      <tr class="tot"><td></td><td></td><td></td><td></td><td></td><td>3</td><td></td><td></td><td>$6,500</td><td>$375</td><td>$3,618</td><td>$3,332</td></tr>
    </table>
    <div class="notes" style="left:10px;top:64px;width:312px">(1) Commitments secured by properties in Michigan operated by Meridian Care under master leases.<br>(2) Commitments are part of the total loan commitment secured by these properties.</div>
    <div class="band" style="top:96px;height:60px"></div>
    <div class="ph" role="img" aria-label="Photograph of a newly expanded care residence exterior with gabled entry" style="left:43px;top:88px;width:117px;height:68px;background:linear-gradient(170deg,#b9cbe3 0%,#d8d8d4 55%,#7c8a6d 100%)"></div>
    <div class="ph" role="img" aria-label="Photograph of a renovated lounge interior" style="left:173px;top:88px;width:108px;height:68px;background:linear-gradient(170deg,#c6b79b 0%,#8d7a60 55%,#5e564c 100%)"></div>
    <div class="caption" style="left:43px;top:90px;width:117px">Parkside Lodge of Richmond · Richmond, MI</div>
    <div class="caption" style="left:173px;top:90px;width:108px">Parkside Lodge of East Lansing</div>
    <div class="ftr"><span>INVESTMENTS</span><span>PAGE | 7</span></div>
  </section>

  <!-- Lease-up -->
  <section class="slide" style="left:13px;top:808px">
    <div class="hdr"><div class="brand"><span class="mark"></span>QUENVAB</div><div class="bar two">REAL ESTATE ACTIVITIES – LEASE-UP<small>(DOLLAR AMOUNTS IN THOUSANDS)</small></div><div class="strip">SUPPLEMENTAL INFORMATION 2Q 2020</div></div>
    <table class="grid" style="left:6px;top:32px;width:318px">
      <tr><th>DATE ACQUIRED</th><th>DATE OPENED</th><th>OCCUPANCY AT 12/31/2019</th><th>DEVELOPMENT COMMIT. YEAR</th><th>PROJECT TYPE</th><th>LOCATION</th><th>OPERATOR</th><th># OF PROJ.</th><th>PROP. TYPE</th><th># BEDS/ UNITS</th><th>INITIAL CASH YIELD</th><th>TOTAL INVESTMENT</th></tr>
      <tr><td>Oct-2016</td><td>Jun-2019</td><td>71%</td><td>2016</td><td>Develop.</td><td>Union, KY</td><td>Harbor</td><td>1</td><td>MC</td><td>60 units</td><td>7.00%</td><td>$14,887</td></tr>
      <tr><td>Sep-2017</td><td>Jul-2019</td><td>53%</td><td>2017</td><td>Develop.</td><td>Salem, OR</td><td>Meridian</td><td>1</td><td>ALF</td><td>116 units</td><td>7.25%</td><td>$21,237</td></tr>
      <tr class="tot"><td></td><td></td><td></td><td></td><td></td><td></td><td></td><td>2</td><td></td><td>176 units</td><td></td><td>$36,124</td></tr>
    </table>
    <div class="notes" style="left:6px;top:55px;width:318px">(1) Represents date of certificate of occupancy.<br>(2) Total investment for these projects includes land and development costs.<br>(3) As a result of market conditions occupancy was lower than expected; rent deferral was granted.<br>(4) Certificate of occupancy received in early 2019 with residents admitted in April.</div>
    <div class="band" style="top:124px;height:42px"></div>
    <div class="ph" role="img" aria-label="Photograph of a bronze statue in front of a modern healthcare centre entrance" style="left:63px;top:91px;width:124px;height:70px;background:linear-gradient(165deg,#7fa3d6 0%,#8b7c6b 55%,#4b5a3e 100%)"></div>
    <div class="caption" style="left:200px;top:140px;text-align:left">Stonebrook Healthcare Center &amp; Rehabilitation<br>Union, KY</div>
    <div class="ftr"><span>INVESTMENTS</span><span>PAGE | 8</span></div>
  </section>

  <!-- Lease-up history -->
  <section class="slide" style="left:351px;top:808px">
    <div class="hdr"><div class="brand"><span class="mark"></span>QUENVAB</div><div class="bar">REAL ESTATE ACTIVITIES – LEASE-UP HISTORY</div><div class="strip">SUPPLEMENTAL INFORMATION 2Q 2020</div></div>
    <div style="position:absolute;left:10px;top:30px;width:310px;height:130px;background:#fff;box-shadow:0 0 3px rgba(0,0,0,.15)"></div>
    <table class="grid" style="left:14px;top:34px;width:302px;font-size:2.1px">
      <tr><th>PROPERTY</th><th>LOCATION</th><th>OPERATOR</th><th>PROP. TYPE</th><th>PROJECT TYPE</th><th># BEDS/ UNITS</th><th>DATE ACQUIRED</th><th>DATE OPENED</th><th>DATE STABILIZED</th><th># MONTHS</th></tr>
      <tr><td>Aspen Place</td><td>Loveland, CO</td><td>Harbor</td><td>MC</td><td>Develop.</td><td>60 units</td><td>Sep-2012</td><td>Jun-2014</td><td>Jun-2015</td><td>12</td></tr>
      <tr><td>Birch Court</td><td>Greeley, CO</td><td>Harbor</td><td>MC</td><td>Develop.</td><td>60 units</td><td>Sep-2012</td><td>Aug-2014</td><td>Mar-2016</td><td>19</td></tr>
      <tr><td>Cedar Place</td><td>Aurora, CO</td><td>Harbor</td><td>MC</td><td>Develop.</td><td>60 units</td><td>Feb-2013</td><td>Dec-2014</td><td>Jan-2016</td><td>13</td></tr>
      <tr><td>Dove Place</td><td>Westminster, CO</td><td>Harbor</td><td>MC</td><td>Develop.</td><td>60 units</td><td>Sep-2013</td><td>Nov-2015</td><td>Feb-2017</td><td>15</td></tr>
      <tr><td>Elm Place</td><td>Burr Ridge, IL</td><td>Harbor</td><td>MC</td><td>Develop.</td><td>66 units</td><td>Sep-2014</td><td>Feb-2016</td><td>Feb-2017</td><td>12</td></tr>
      <tr><td>Fern Place</td><td>Overland, KS</td><td>Harbor</td><td>MC</td><td>Develop.</td><td>60 units</td><td>Sep-2014</td><td>Jul-2016</td><td>Aug-2018</td><td>24</td></tr>
      <tr><td>Grove Place</td><td>Frisco, TX</td><td>Harbor</td><td>MC</td><td>Develop.</td><td>66 units</td><td>Apr-2015</td><td>Jan-2017</td><td>Jun-2018</td><td>17</td></tr>
      <tr><td>Hazel Park</td><td>Union, KY</td><td>Harbor</td><td>SNF</td><td>Develop.</td><td>143 beds</td><td>Sep-2016</td><td>Nov-2018</td><td>Dec-2019</td><td>13</td></tr>
      <tr><td>Iris Gardens</td><td>Tulsa, OK</td><td>Meridian</td><td>ALF</td><td>Re-develop.</td><td>100 beds</td><td>Sep-2011</td><td>Jan-2013</td><td>Jan-2014</td><td>12</td></tr>
      <tr><td>Juniper Creek</td><td>Mesa, AZ</td><td>Meridian</td><td>ALF</td><td>Acquis.</td><td>84 units</td><td>Apr-2016</td><td>Apr-2016</td><td>Mar-2017</td><td>11</td></tr>
      <tr><td>Kestrel Way</td><td>Davis, CA</td><td>Meridian</td><td>ALF</td><td>Acquis.</td><td>92 units</td><td>Jun-2017</td><td>Jun-2017</td><td>Jun-2018</td><td>12</td></tr>
      <tr><td>Laurel Ridge</td><td>Waco, TX</td><td>Harbor</td><td>MC</td><td>Develop.</td><td>48 units</td><td>Sep-2015</td><td>Jul-2017</td><td>Jun-2019</td><td>23</td></tr>
      <tr><td>Maple Lane</td><td>Wichita, KS</td><td>Harbor</td><td>ALF</td><td>Develop.</td><td>77 units</td><td>Oct-2015</td><td>Sep-2017</td><td>Jun-2019</td><td>21</td></tr>
      <tr><td>Oak Terrace</td><td>Dallas, TX</td><td>Harbor</td><td>ILF</td><td>Develop.</td><td>108 units</td><td>Mar-2016</td><td>Nov-2017</td><td>Nov-2019</td><td>24</td></tr>
    </table>
    <div class="notes" style="left:12px;top:162px;width:306px">(1) Represents date of certificate of occupancy. (2) Property stabilized after reaching 80% occupancy for three consecutive months.</div>
    <div class="ftr"><span>INVESTMENTS</span><span>PAGE | 9</span></div>
  </section>

  <!-- Portfolio overview -->
  <section class="slide" style="left:690px;top:808px">
    <div class="hdr"><div class="brand"><span class="mark"></span>QUENVAB</div><div class="bar two">PORTFOLIO OVERVIEW<small>(DOLLAR AMOUNTS IN THOUSANDS)</small></div><div class="strip">SUPPLEMENTAL INFORMATION 2Q 2020</div></div>
    <table class="grid" style="left:14px;top:36px;width:306px">
      <tr><th>PROPERTY TYPE</th><th># OF PROPERTIES</th><th>GROSS INVESTMENT</th><th>% OF INVESTMENT</th><th>RENTAL INCOME</th><th>INTEREST INCOME</th><th>% OF REVENUES</th></tr>
      <tr><td>Skilled Nursing</td><td>82</td><td>$742,400</td><td>38.2%</td><td>$69,287</td><td>$28,981</td><td>48.7%</td></tr>
      <tr><td>Assisted Living</td><td>105</td><td>$898,100</td><td>48.1%</td><td>$86,011</td><td>–</td><td>43.7%</td></tr>
      <tr><td>Under Development</td><td>–</td><td>$17,600</td><td>1.2%</td><td>–</td><td>–</td><td>–</td></tr>
      <tr><td>Other</td><td>1</td><td>$11,300</td><td>0.7%</td><td>$932</td><td>–</td><td>0.5%</td></tr>
      <tr class="tot"><td>Total</td><td>188</td><td>$1,669,400</td><td>100%</td><td>$156,230</td><td>$28,981</td><td>100%</td></tr>
    </table>
    <div class="notes" style="left:14px;top:70px;width:306px">(1) Includes rental income and interest from mortgage loans and notes receivable.<br>(2) Includes interest income from mortgage loans and mezzanine financing.<br>(3) Includes development projects and land parcels held for future development.</div>
    <svg style="position:absolute;left:16px;top:100px" width="80" height="70" viewBox="0 0 80 70">
      <circle cx="28" cy="37" r="24" fill="#233c8c"/>
      <path d="M28 37 L28 13 A24 24 0 0 1 47.2 22.6 Z" fill="#3f7ad0"/>
      <line x1="44" y1="20" x2="52" y2="10" stroke="#7a8" stroke-width=".3"/>
      <text x="52" y="9" font-size="3" fill="#3f63b8" font-family="Open Sans, sans-serif">Loans Receivable</text>
      <text x="52" y="13" font-size="3" fill="#3f63b8" font-family="Open Sans, sans-serif">14.7%</text>
      <text x="46" y="62" font-size="3" fill="#233c8c" font-family="Open Sans, sans-serif">Gross Real Property</text>
      <text x="46" y="66" font-size="3" fill="#233c8c" font-family="Open Sans, sans-serif">85.3%</text>
    </svg>
    <div class="hex" style="left:135px;top:108px">
      <svg width="48" height="54" viewBox="0 0 48 54"><polygon points="24,2 46,14 46,40 24,52 2,40 2,14" fill="#fff" stroke="#233c8c" stroke-width="3"/></svg>
      <div class="t"><span style="font-size:9px">28</span><span style="font-size:8px">States</span></div>
    </div>
    <div class="hex" style="left:188px;top:102px">
      <svg width="48" height="54" viewBox="0 0 48 54"><polygon points="24,2 46,14 46,40 24,52 2,40 2,14" fill="#fff" stroke="#233c8c" stroke-width="2"/></svg>
      <div class="t" style="font-size:3.4px;line-height:4.6px"><span>199</span><span>Properties</span><span>2</span><span>Development projects</span><span>3</span><span>Land parcels</span></div>
    </div>
    <div class="hex" style="left:243px;top:108px">
      <svg width="48" height="54" viewBox="0 0 48 54"><polygon points="24,2 46,14 46,40 24,52 2,40 2,14" fill="#fff" stroke="#233c8c" stroke-width="3"/></svg>
      <div class="t"><span style="font-size:9px">30</span><span style="font-size:6px">Operators</span></div>
    </div>
    <div class="ftr"><span>INVESTMENTS</span><span>PAGE | 10</span></div>
  </section>

  <!-- Geography -->
  <section class="slide" style="left:351px;top:1003px">
    <div class="hdr"><div class="brand"><span class="mark"></span>QUENVAB</div><div class="bar">PORTFOLIO DIVERSIFICATION – GEOGRAPHY</div><div class="strip">SUPPLEMENTAL INFORMATION 2Q 2020</div></div>
    <p style="position:absolute;left:60px;top:34px;width:200px;text-align:center;font-size:3.8px;line-height:5px;color:var(--blue)">States in which we have the highest concentration of properties are those states with the highest projected increases in the 80+ population cohort over the next decade.</p>
    <div class="ph" role="img" aria-label="Map of the United States with states shaded light and mid blue, marked with numbered property counts" style="left:14px;top:52px;width:230px;height:125px;background:radial-gradient(ellipse at 50% 55%,#8ec0ef 0%,#b6d5f3 55%,#d8d8dc 85%,#fff 100%)"></div>
    <div class="legend" style="left:252px;top:84px;width:72px">
      <div><i style="background:#2d6fc9;border-radius:50%"></i>Skilled Nursing (82)</div>
      <div><i style="background:var(--navy)"></i>Assisted Living (105)</div>
      <div><i style="background:#222;transform:rotate(45deg)"></i>Other (1)</div>
      <div><i style="background:#777"></i>Under Development (2)</div>
      <div><i style="background:#fff;border:.4px solid #3f63b8"></i>Land (3)</div>
      <div style="font-size:2.2px;line-height:3px;margin-top:2px">* Behavioral health care hospital</div>
      <div style="font-size:2.2px;line-height:3px;margin-top:3px"><i style="background:#9cc7f0"></i>Represents 10 states with the highest projected increases in the 80+ population cohort from 2020 to 2030.</div>
      <div style="font-size:2.2px;line-height:3px;margin-top:2px">Source: Regional Senior Housing Association, 2019 Population Growth Forecast by State.</div>
    </div>
    <div class="ftr"><span>INVESTMENTS</span><span>PAGE | 11</span></div>
  </section>

</div>
</body>
</html>
```